Fish Farm needing 3 - Fold Flyer / Price List designed

We are looking for a new Price List for our Fish Farm. I have attached an example of the basic info that needs in the flyer. We want the flyer to be a 3 fold page. Anything that is on our website, you can use for ideas. There are some pictures on there that can be photoshopped into the flyer. Do not use any photos from any other sites. We are looking for something professional but fun and exciting! I have also attached our business logo. We tend to stay with the blues and greens for colors. Let's get started....
Updates

Need extra days to review

Contact Information for Business Card

We are needing a business card with our new logo on it. We also need our address, phone numbers, email address, and website listed. Please view our website for more ideas.

Colors

```html
<!DOCTYPE html>
<html lang="en">
<head>
<meta charset="utf-8">
<title>Fish Price List – Tri-fold</title>
<link rel="stylesheet" href="https://fonts.googleapis.com/css2?family=Montserrat:wght@400;500;600;700&display=swap">
<style>
  :root {
    --ink: #1c1c1e;
    --deep-blue: #1f4f8c;
    --mid-blue: #3a78b8;
    --soft-blue: #7eb0d9;
    --paper: #f3f3f4;
    --paper-edge: #e4e4e6;
    --brand: #1e3f96;
  }
  * { margin: 0; padding: 0; box-sizing: border-box; }
  html, body { width: 1200px; height: 852px; overflow: hidden; background: #ffffff; }
  body { font-family: "Montserrat", sans-serif; color: var(--ink); }

  .flyer {
    position: relative; width: 1200px; height: 852px; overflow: hidden;
    background: linear-gradient(90deg, var(--paper) 0%, #fafafa 32%, var(--paper-edge) 33.4%, var(--paper) 34%, #fbfbfb 66%, var(--paper-edge) 66.7%, var(--paper) 67.2%, #fafafa 100%);
  }

  .band { position: absolute; left: 0; width: 1200px; }
  .band-top { top: 0; height: 78px; background: linear-gradient(90deg, var(--mid-blue) 0%, var(--soft-blue) 50%, var(--deep-blue) 100%); }
  .band-bottom { bottom: 0; height: 50px; background: linear-gradient(90deg, var(--deep-blue) 0%, var(--soft-blue) 50%, var(--mid-blue) 100%); }
  .rule { position: absolute; left: 0; width: 1200px; height: 1px; background: #5a93cc; }
  .rule-top { top: 88px; }
  .rule-bottom { top: 796px; }

  .section { position: absolute; text-align: center; }
  .heading { font-weight: 600; font-size: 17px; line-height: 20px; letter-spacing: 0.2px; }
  .sub { font-size: 13px; line-height: 16px; margin-top: 1px; }
  .line { font-size: 17.5px; line-height: 23px; }

  .grid { display: grid; font-size: 17.5px; line-height: 19px; margin-top: 4px; }
  .grid span { text-align: center; white-space: nowrap; }

  .hybrid { left: 60px; top: 100px; width: 280px; }
  .hybrid .grid { grid-template-columns: 82px 76px 56px 66px; margin-left: -2px; }

  .regular { left: 60px; top: 252px; width: 280px; }
  .regular .grid { grid-template-columns: 100px 72px 72px; justify-content: center; margin-left: 6px; }

  .redear { left: 60px; top: 364px; width: 280px; }
  .redear .grid { grid-template-columns: 100px 76px 68px; justify-content: center; margin-left: 6px; }

  .bass { left: 60px; top: 495px; width: 280px; }
  .bass .grid { grid-template-columns: 110px 100px; justify-content: center; }

  .note { position: absolute; left: 103px; top: 642px; font-size: 11px; font-weight: 600; line-height: 13.5px; }

  .carp { left: 440px; top: 101px; width: 312px; }
  .carp-rows { text-align: left; margin-top: 12px; margin-left: 28px; }
  .carp-rows .row { display: flex; font-size: 17.5px; line-height: 23px; }
  .carp-rows .qty { width: 166px; }
  .carp-rows .row.minimum .qty { width: 96px; }
  .carp-rows .row.inquire .price { padding-left: 19px; }

  .channel { left: 460px; top: 315px; width: 272px; }
  .channel .grid { grid-template-columns: 84px 76px 60px; justify-content: center; margin-left: -14px; }

  .albino { left: 460px; top: 416px; width: 272px; }
  .albino .grid, .crappie .grid { grid-template-columns: 98px 98px; justify-content: center; margin-top: 8px; }

  .crappie { left: 460px; top: 538px; width: 272px; }

  .minnows { left: 460px; top: 664px; width: 272px; }

  .brand { position: absolute; left: 446px; top: 762px; width: 300px; text-align: center;
    font-weight: 700; font-size: 16px; letter-spacing: 0.4px; color: var(--brand); }

  .shiners { left: 860px; top: 104px; width: 280px; }
  .shiners .grid, .tilapia .grid { grid-template-columns: 110px 120px; justify-content: center; line-height: 23px; margin-top: 2px; }

  .food { left: 860px; top: 205px; width: 280px; }

  .tilapia { left: 860px; top: 346px; width: 280px; }
  .tilapia .line { margin-top: 2px; }

  .koi { left: 860px; top: 529px; width: 280px; }
  .koi .grid { grid-template-columns: 120px 140px; justify-content: center; line-height: 23px; margin-top: 2px; }

  .butterfly { left: 860px; top: 678px; width: 280px; }

  .disclaimer { position: absolute; left: 820px; top: 774px; width: 360px; text-align: center;
    font-size: 11px; font-weight: 600; letter-spacing: 0.1px; }
</style>
</head>
<body>
<main class="flyer">
  <div class="band band-top" role="img" aria-label="Blue wave band across the top"></div>
  <div class="rule rule-top"></div>
  <div class="band band-bottom" role="img" aria-label="Blue wave band across the bottom"></div>
  <div class="rule rule-bottom"></div>

  <!-- Left panel -->
  <section class="section hybrid">
    <h2 class="heading">HYBRID BLUEGILL<br>(HYBRID SUNFISH)</h2>
    <div class="grid">
      <span>Size</span><span>Each</span><span>1000</span><span>3000</span>
      <span>1-3 Inch</span><span>50¢</span><span>45¢</span><span>40¢</span>
      <span>3-5 Inch</span><span>80¢</span><span>75¢</span><span></span>
      <span>*5-7 Inch</span><span>$1.75</span><span></span><span></span>
    </div>
  </section>

  <section class="section regular">
    <h2 class="heading">REGULAR BLUEGILL</h2>
    <div class="grid">
      <span>Size</span><span>Each</span><span>1000</span>
      <span>1-3 Inch</span><span>50¢</span><span>45¢</span>
      <span>*3-5 Inch</span><span>80¢</span><span>75¢</span>
    </div>
  </section>

  <section class="section redear">
    <h2 class="heading">REDEAR SUNFISH</h2>
    <div class="grid">
      <span>Size</span><span>Each</span><span>1000</span>
      <span>1-3 Inch</span><span>50¢</span><span>45¢</span>
      <span>3-4 Inch</span><span>75¢</span><span>70¢</span>
      <span>*4-5 Inch</span><span>$1.00</span><span>95¢</span>
    </div>
  </section>

  <section class="section bass">
    <h2 class="heading">LARGEMOUTH BASS</h2>
    <div class="grid">
      <span>Size</span><span>Each</span>
      <span>3 Inch</span><span>$1.10</span>
      <span>3-4 Inch</span><span>$1.20</span>
      <span>*4-6 Inch</span><span>$1.95</span>
      <span>*6-8 Inch</span><span>$2.75</span>
    </div>
  </section>

  <p class="note">*When Available.<br>&nbsp;Sizes Vary Depending on Time of Year</p>

  <!-- Middle panel -->
  <section class="section carp">
    <h2 class="heading">TRIPLOID<br>GRASS CARP</h2>
    <p class="sub">(Indiana Prices)</p>
    <div class="carp-rows">
      <div class="row minimum"><span class="qty">8-11 Inch</span><span class="price">Minimum 5</span></div>
      <div class="row"><span class="qty">5-24 Grass Carp</span><span class="price">$16.00 each</span></div>
      <div class="row"><span class="qty">25-49 Grass Carp</span><span class="price">$15.00 each</span></div>
      <div class="row"><span class="qty">50-99 Grass Carp</span><span class="price">$14.00 each</span></div>
      <div class="row inquire"><span class="qty">100+ Grass Carp</span><span class="price">Inquire</span></div>
    </div>
  </section>

  <section class="section channel">
    <h2 class="heading">CHANNEL CATFISH</h2>
    <div class="grid">
      <span>Size</span><span>Each</span><span>1000</span>
      <span>6-8 Inch</span><span>65¢</span><span>60¢</span>
    </div>
  </section>

  <section class="section albino">
    <h2 class="heading">ALBINO CATFISH</h2>
    <p class="sub">(March &amp; April)</p>
    <div class="grid">
      <span>Size</span><span>Each</span>
      <span>5-8 Inch</span><span>$1.20</span>
    </div>
  </section>

  <section class="section crappie">
    <h2 class="heading">BLACK CRAPPIE</h2>
    <p class="sub">(March &amp; April)</p>
    <div class="grid">
      <span>Size</span><span>Each</span>
      <span>3-5 Inch</span><span>$1.10</span>
    </div>
  </section>

  <section class="section minnows">
    <h2 class="heading">FATHEAD MINNOWS</h2>
    <p class="line">$36.00 per thousand</p>
    <p class="line">($9.00 per lb.)</p>
  </section>

  <p class="brand">BROOKLINE FISH FARM</p>

  <!-- Right panel -->
  <section class="section shiners">
    <h2 class="heading">GOLDEN SHINERS</h2>
    <p class="sub">(Delivery Only – Minimum 50 lb.)</p>
    <div class="grid">
      <span>50-99 lb.</span><span>$8.00 lb.</span>
      <span>100+ lb.</span><span>$7.50 lb.</span>
    </div>
  </section>

  <section class="section food">
    <h2 class="heading">FLOATING FISH FOOD</h2>
    <p class="line">Starter Size (50 lb. Bag)</p>
    <p class="line">41% Protein</p>
    <p class="line">Market Price – Inquire</p>
    <p class="line">(Only Available at Farm)</p>
  </section>

  <section class="section tilapia">
    <h2 class="heading">TILAPIA</h2>
    <p class="sub">(May 15 – June 30)</p>
    <p class="line">5-10 Tilapia per lb.</p>
    <div class="grid">
      <span>1-25 lb.</span><span>$15.00 lb.</span>
      <span>26-40 lb.</span><span>$14.00 lb.</span>
      <span>40-50 lb.</span><span>$13.00 lb.</span>
      <span>50+ lb.</span><span>$12.00 lb.</span>
    </div>
  </section>

  <section class="section koi">
    <h2 class="heading">JAPANESE KOI</h2>
    <div class="grid">
      <span>Size</span><span>Each</span>
      <span>4-5 Inch</span><span>$6.00</span>
      <span>6-8 Inch</span><span>$10.00</span>
      <span>*9-12 Inch</span><span>$15.00</span>
    </div>
  </section>

  <section class="section butterfly">
    <h2 class="heading">BUTTERFLY KOI<br>ALSO AVAILABLE!</h2>
  </section>

  <p class="disclaimer">PRICES SUBJECT TO CHANGE WITHOUT NOTICE</p>
</main>
</body>
</html>
```